高単価、会員制の予備校になります。
定員MAX20名。
浪人生には受験職人が担任となり、授業だけでなく普段の自習や生活態度の面倒を見て合格を目指していきます。
高校生には学校が終わった後の生活の学習の面倒を見ていきます。

「高級感」「独自性」「受験職人」

がキーワードだと思っています。
1.大学受験コンサルティング
2.医学部/難関大学専門
3.会社のロゴを入れる(少しアレンジして高級感を出すとより良い)

サイズ(横:縦=500mm:2000mm)多少の変更があっても問題無いです。
赤系、赤、白、黒(少し)
今会社で使用しているロゴを添付しています。
壁看板に塾名は入れるので今回の看板に塾名は入れなくても良いです。
ロゴは入れて欲しいです。

一番初めのデザインが良かったのと、その後の細かい修正点などを丁寧に対応していただいた点で選びました。

今回提案して頂いてありがとうございました。
看板のデザインを考えながら「魅せ方」をいろいろ考える事ができたので勉強になりました。
またお願いすると思いますのでその時もよろしくお願いいたします。

```html
<!DOCTYPE html>
<html lang="ja">
<head>
<meta charset="utf-8">
<title>大学受験コンサルティング 縦型看板</title>
<link href="https://fonts.googleapis.com/css2?family=Noto+Sans+JP:wght@700;900&family=Noto+Serif+JP:wght@500&display=swap" rel="stylesheet">
<style>
  :root {
    --brand-red: #c8202e;
    --deep-red: #8e1a24;
    --ink: #2b2b2b;
    --paper: #ffffff;
  }
  html, body {
    margin: 0;
    padding: 0;
    width: 1200px;
    height: 3744px;
    overflow: hidden;
    background: var(--paper);
  }
  .signboard {
    position: relative;
    width: 1200px;
    height: 3744px;
    background: var(--paper);
    overflow: hidden;
  }
  .stripes {
    position: absolute;
    inset: 0;
  }
  .headline {
    position: absolute;
    margin: 0;
    writing-mode: vertical-rl;
    font-family: "Noto Sans JP", sans-serif;
    font-weight: 900;
    color: var(--brand-red);
    line-height: 1;
  }
  .headline--exam {
    left: 775px;
    top: 140px;
    font-size: 205px;
    letter-spacing: -2px;
  }
  .headline--consulting {
    left: 305px;
    top: 410px;
    font-size: 232px;
    letter-spacing: 2px;
  }
  .specialty {
    position: absolute;
    left: 715px;
    top: 960px;
    margin: 0;
    writing-mode: vertical-rl;
    font-family: "Noto Serif JP", serif;
    font-weight: 500;
    font-size: 138px;
    line-height: 1.3;
    color: var(--ink);
  }
  .brand {
    position: absolute;
    left: 0;
    right: 0;
    top: 3080px;
    display: flex;
    align-items: center;
    justify-content: center;
    gap: 40px;
  }
  .brand__mark {
    width: 110px;
    height: 110px;
    background: var(--brand-red);
  }
  .brand__name {
    font-family: "Noto Sans JP", sans-serif;
    font-weight: 900;
    font-size: 150px;
    color: var(--brand-red);
    letter-spacing: 10px;
    line-height: 1;
  }
</style>
</head>
<body>
  <main class="signboard">
    <svg class="stripes" width="1200" height="3744" viewBox="0 0 1200 3744" aria-hidden="true">
      <!-- top corner accent -->
      <polygon points="0,300 500,0 560,0 0,340" fill="var(--brand-red)"/>
      <polygon points="0,230 385,0 405,0 0,244" fill="var(--deep-red)"/>
      <!-- central diagonal band -->
      <polygon points="0,2620 1200,1920 1200,1940 0,2640" fill="var(--brand-red)"/>
      <polygon points="0,2700 1200,2000 1200,2068 0,2768" fill="var(--deep-red)"/>
      <polygon points="0,2800 1200,2100 1200,2120 0,2820" fill="var(--brand-red)"/>
    </svg>

    <h1 class="headline headline--exam">大学受験</h1>
    <h2 class="headline headline--consulting">コンサルティング</h2>

    <p class="specialty">難関大学専門<br>医学部／</p>

    <div class="brand">
      <span class="brand__mark"></span>
      <span class="brand__name">明峰義塾</span>
    </div>
  </main>
</body>
</html>
```